Construction Company Business Card

Business Card Design using new Logo

Contact Information for Business Card

include all company info and website

Requirements
Must have
• Marlon Ridgeway - President
ph. 254-716-5093
Cedar Bluff, TX
marlon@stonefieldworks.com
www.stonefieldworks.com

```html
<!DOCTYPE html>
<html lang="en">
<head>
<meta charset="utf-8">
<title>Stonefield Works – Business Card</title>
<link rel="stylesheet" href="https://fonts.googleapis.com/css2?family=Montserrat:wght@400;500;600&display=swap">
<style>
  :root {
    --page: #efeeef;
    --card: #ffffff;
    --red: #bf2126;
    --red-deep: #8f171b;
    --grey: #8e8f94;
    --grey-light: #b7b8bd;
    --rule: #6f6f73;
  }
  * { margin: 0; padding: 0; box-sizing: border-box; }
  html, body {
    width: 1146px; height: 1200px; overflow: hidden;
    background: var(--page);
    font-family: "Montserrat", sans-serif;
  }
  .card {
    position: absolute;
    width: 764px; height: 440px;
    border-radius: 38px;
    overflow: hidden;
  }
  .card--front { left: 189px; top: 153px; background: var(--card); }
  .card--back { left: 170px; top: 629px; background: var(--red); }

  .brand {
    position: absolute;
    display: flex; align-items: center; gap: 10px;
    font-weight: 500; white-space: nowrap;
  }
  .card--front .brand {
    left: 72px; width: 296px; top: 196px; justify-content: center;
    font-size: 21px; letter-spacing: 1px; color: var(--grey-light);
  }
  .brand__mark { width: 12px; height: 12px; background: var(--red); flex: none; }
  .card--back .brand {
    left: 0; right: 0; top: 196px; justify-content: center;
    font-size: 40px; color: var(--red-deep); letter-spacing: 2px;
  }

  .divider {
    position: absolute; left: 382px; top: 130px;
    width: 1.5px; height: 180px; background: var(--rule);
  }
  .contact { position: absolute; left: 397px; top: 122px; color: var(--grey); }
  .contact__name { font-size: 27px; line-height: 32px; font-weight: 400; color: var(--grey); }
  .contact__name b { font-weight: 600; color: var(--red); }
  .contact__role { font-size: 19px; line-height: 22px; font-weight: 500; }
  .contact__place { font-size: 19px; margin-top: 19px; font-weight: 500; }
  .contact__list { list-style: none; margin-top: 20px; }
  .contact__list li {
    display: flex; align-items: center; gap: 9px;
    font-size: 19px; line-height: 26px; font-weight: 500;
  }
  .contact__list svg { width: 14px; height: 14px; fill: var(--red); flex: none; }

  .band { position: absolute; left: 0; bottom: 0; width: 764px; height: 17px; }
</style>
</head>
<body>
  <section class="card card--front">
    <div class="brand"><span class="brand__mark"></span>STONEFIELD WORKS</div>
    <div class="divider"></div>
    <div class="contact">
      <p class="contact__name"><b>Marlon</b> Ridgeway</p>
      <p class="contact__role">President</p>
      <p class="contact__place">Cedar Bluff, TX</p>
      <ul class="contact__list">
        <li><svg viewBox="0 0 16 16"><path d="M3.5 1.5l2.6 2.8-1.5 1.9c.9 2 2.6 3.6 4.6 4.6l1.9-1.5 2.8 2.6-1.6 2.3C7.6 14 2 8.4 1.2 3.1z"/></svg>254-716-5093</li>
        <li><svg viewBox="0 0 16 16"><path d="M1 3h14v10H1z M2 4.2v.6l6 4 6-4v-.6z" fill-rule="evenodd"/></svg>marlon@stonefieldworks.com</li>
        <li><svg viewBox="0 0 16 16"><circle cx="8" cy="8" r="7"/><path d="M1.5 8h13M8 1.2c-2.4 2-2.4 11.6 0 13.6M8 1.2c2.4 2 2.4 11.6 0 13.6" stroke="#fff" stroke-width="1.1" fill="none"/></svg>www.stonefieldworks.com</li>
      </ul>
    </div>
    <svg class="band" viewBox="0 0 764 17" preserveAspectRatio="none">
      <polygon points="0,0 392,0 374,17 0,17" fill="var(--red)"/>
      <polygon points="398,0 764,0 764,17 380,17" fill="var(--grey-light)"/>
    </svg>
  </section>

  <section class="card card--back">
    <div class="brand">STONEFIELD WORKS</div>
  </section>
</body>
</html>
```